Re-design of website

I have an existing website that I would like to improve. The functionality will remain the same but the overall look will need to be changed. I have some ideas of what i would like included and am also in need of someone else to input their own creative ideas. I am on a tight deadline to get these improvements made as I have many people being directed to the site via our advertising campaigns that are in full swing late next week. Thanks
Target Market(s)
The website provides a virtual space for families to learn more about our learning program which we operate out of Dubai and will soon spread to the other Emirates. The families are generally between 25-50 year old parents with children up to the age of 6. They are local Emirati's as well as expats.

```html
<!DOCTYPE html>
<html lang="en">
<head>
<meta charset="utf-8">
<title>Bright Sprouts – Home</title>
<link href="https://fonts.googleapis.com/css2?family=Delius&family=Mali:wght@600&display=swap" rel="stylesheet">
<style>
  :root {
    --sun-light: #ffd43a;
    --sun-mid: #ffc21f;
    --sun-deep: #ffa514;
    --page-grey: #f2f2f2;
    --card-white: #ffffff;
    --orange: #f26522;
    --pink: #e4507f;
    --mission-yellow: #ffd340;
    --body-text: #7b6f8c;
    --footer-text: #7d7a86;
    --lavender: #e9e4ff;
  }
  * { box-sizing: border-box; margin: 0; padding: 0; }
  html, body { width: 1200px; height: 768px; overflow: hidden; }
  body {
    position: relative;
    font-family: "Delius", "Comic Sans MS", cursive;
    background: var(--page-grey);
  }
  .header-field {
    position: absolute; left: 0; top: 0; width: 1200px; height: 374px;
    background: radial-gradient(circle at 600px 110px, var(--sun-light) 0%, var(--sun-mid) 45%, var(--sun-deep) 100%);
  }
  .main-nav { position: absolute; top: 0; left: 0; width: 1200px; height: 60px; }
  .nav-item {
    position: absolute; top: 16px; width: 117px; height: 42px;
    border: 3px solid #fff; border-radius: 8px;
    background: linear-gradient(#ff8a2c, #f86a14);
    color: #fff; font-family: "Mali", "Comic Sans MS", cursive; font-weight: 600;
    font-size: 16px; line-height: 36px; text-align: center; text-decoration: none;
    white-space: nowrap;
    box-shadow: 0 2px 3px rgba(150,80,0,0.3);
  }
  .nav-item::before {
    content: ""; position: absolute; top: -12px; left: 50%; width: 10px; height: 10px;
    margin-left: -5px; border: 2px solid #fff; border-radius: 50%;
  }
  .nav-item.is-active { background: linear-gradient(#ef5a8c, #e03a72); }
  .brand-name {
    position: absolute; top: 76px; left: 0; width: 1200px; text-align: center;
    font-family: "Mali", "Comic Sans MS", cursive; font-weight: 600;
    font-size: 38px; line-height: 48px; color: var(--pink);
  }
  .tagline {
    position: absolute; top: 133px; left: 0; width: 1200px; text-align: center;
    font-size: 20px; color: var(--lavender);
    text-shadow: 0 0 2px #7a5bb0, 1px 1px 1px #7a5bb0;
  }
  .content-card {
    position: absolute; left: 128px; top: 179px; width: 950px; height: 456px;
    background: var(--card-white); border-radius: 18px;
  }
  .content-card::before {
    content: ""; position: absolute; left: 6px; top: 6px; right: 6px; height: 260px;
    border-radius: 14px 14px 0 0;
    background: linear-gradient(#f4f4f4, rgba(255,255,255,0));
  }
  .card-shadow { position: absolute; left: 150px; top: 630px; width: 906px; height: 20px; }
  .welcome-title {
    position: absolute; left: 158px; top: 200px;
    font-family: "Mali", "Comic Sans MS", cursive; font-weight: 600;
    font-size: 31px; color: var(--orange);
  }
  .welcome-text {
    position: absolute; left: 158px; top: 249px; width: 512px;
    font-size: 13px; line-height: 18px; color: var(--body-text); text-align: justify;
  }
  .welcome-text p + p { margin-top: 18px; }
  .welcome-text strong { font-weight: 400; color: #5e5370; }
  .divider {
    position: absolute; left: 158px; top: 432px; width: 511px;
    border-top: 1px dashed #cfcfcf;
  }
  .mission-box {
    position: absolute; left: 702px; top: 211px; width: 348px; height: 222px;
    background: var(--pink); border-radius: 16px; padding: 12px 28px 0 24px;
  }
  .mission-title {
    font-family: "Mali", "Comic Sans MS", cursive; font-weight: 600;
    font-size: 30px; line-height: 34px; color: var(--mission-yellow);
  }
  .mission-text {
    margin-top: 9px; font-size: 13px; line-height: 18px; color: #fff; text-align: justify;
  }
  .talent { position: absolute; top: 458px; width: 160px; text-align: center; }
  .talent-art {
    display: block; margin: 0 auto; width: 90px; height: 120px; border-radius: 40px 40px 20px 20px;
  }
  .talent-label {
    margin-top: 8px; font-family: "Mali", "Comic Sans MS", cursive; font-weight: 600;
    font-size: 16.5px; color: var(--orange);
  }
  .talent.is-you .talent-label { color: var(--pink); }
  .copyright {
    position: absolute; top: 661px; left: 0; width: 1200px; text-align: center;
    font-size: 14px; color: var(--footer-text);
  }
  .phone {
    position: absolute; top: 686px; left: 0; width: 1200px; text-align: center;
    font-size: 20px; color: var(--pink);
  }
  .social { position: absolute; top: 719px; left: 546px; display: flex; gap: 11px; }
  .social a { display: block; width: 31px; height: 31px; border-radius: 50%; }
  .social .s-one { background: #4a6aa8; }
  .social .s-two { background: #38bfe8; }
  .social .s-mail { background: #dcdcdc; }
</style>
</head>
<body>
  <div class="header-field"></div>

  <nav class="main-nav">
    <a class="nav-item is-active" style="left:129px">Home</a>
    <a class="nav-item" style="left:268px">Our Method</a>
    <a class="nav-item" style="left:406px">The Program</a>
    <a class="nav-item" style="left:545px">Media</a>
    <a class="nav-item" style="left:684px">About Us</a>
    <a class="nav-item" style="left:822px">Contact Us</a>
    <a class="nav-item" style="left:961px">News</a>
  </nav>

  <div class="brand-name">Bright Sprouts</div>
  <div class="tagline">Register Your Interest Today</div>

  <svg class="card-shadow" viewBox="0 0 906 20" aria-hidden="true">
    <path d="M0 4 Q453 -4 906 4 L904 10 Q900 18 880 18 Q453 8 26 18 Q6 18 2 10 Z" fill="#c9c9c9"/>
  </svg>
  <div class="content-card"></div>

  <h1 class="welcome-title">Welcome to Our Site</h1>
  <div class="welcome-text">
    <p>Research and leading academics agree that the early years of a child's life (defined as the 6 month old to 6 year old age group) is a critical time period to enhance the emotional and intellectual IQ of a child. <strong>80%</strong> of your child's brain is developed by the age of 6 years old, to not offer heightened stimulation and specifically, right brain training during this period means that your child will not use a high proportion of their brain in their life time.</p>
    <p>Bright Sprouts Accelerated Learning Centre is the first a whole brain training program designed to maximise your child's potential during this key period of development.</p>
  </div>
  <div class="divider"></div>

  <aside class="mission-box">
    <h2 class="mission-title">Our Mission</h2>
    <p class="mission-text">At <b>Bright Sprouts</b>, our philosophy and curriculum supports like-minded parents who want happiness for their children and want to see their children become the best they can be in their life. Our children are happy, confident and content with inquisitive minds and life skills that form the foundation of their lifetime of development and learning.</p>
  </aside>

  <div class="talent" style="left:130px">
    <div class="talent-art" role="img" aria-label="Illustration of a girl holding a paint palette and brush" style="background:linear-gradient(#f2b48a,#f6e78a)"></div>
    <div class="talent-label">Artise Ability</div>
  </div>
  <div class="talent" style="left:344px">
    <div class="talent-art" role="img" aria-label="Illustration of a boy holding a pinwheel" style="background:linear-gradient(#f6d36a,#3fb9b0)"></div>
    <div class="talent-label">Sharp Imagination</div>
  </div>
  <div class="talent is-you" style="left:541px">
    <div class="talent-art" role="img" aria-label="Pink silhouette of a child with arms raised" style="background:var(--pink)"></div>
    <div class="talent-label">Your Kid</div>
  </div>
  <div class="talent" style="left:717px">
    <div class="talent-art" role="img" aria-label="Illustration of a dancing girl in a green dress" style="background:linear-gradient(#5a3a2a,#b9d86a)"></div>
    <div class="talent-label">Dance Ability</div>
  </div>
  <div class="talent" style="left:913px">
    <div class="talent-art" role="img" aria-label="Illustration of a boy playing football" style="background:linear-gradient(#f1c27d,#e05a2a)"></div>
    <div class="talent-label">Sports Talent</div>
  </div>

  <footer>
    <div class="copyright">Copyright © 2013 Bright Sprouts. All Right Reserved.</div>
    <div class="phone">Tel : +971 500 012 345</div>
    <div class="social">
      <a class="s-one" aria-label="Social page one"></a>
      <a class="s-two" aria-label="Social page two"></a>
      <a class="s-mail" aria-label="Email"></a>
    </div>
  </footer>
</body>
</html>
```